IT’S NOT A CLEANING, IT’S YOUR LIFE! TOP TEN REASONS WHY THIS IS NOT JUST A “CLEANING”

We made a list for our patients to let them know why our hygiene appointments are different than other cleanings. Since this is a lot of information, we would like it easily readable within 4-5 feet but we do not want the post to be HUGE. Please see below:

IT’S NOT A CLEANING, IT’S YOUR LIFE!
TOP TEN REASONS WHY THIS IS NOT JUST A “CLEANING”

10. We make you look better. Healthy teeth and gums are more attractive. Recent studies
show that the smile is the first thing people notice and that people with better looking teeth
are more confident and successful.

9. We can relieve your headaches. During your hygiene visit we evaluate for serious bite
issues, many of which lead to muscle soreness, headaches, and migraines.

8. We check for oral cancer. Oral cancer kills 1 person per hour 24 hours a day. The death rate for oral cancer is higher than cancers we routinely hear about such as cervical, thyroid and skin cancer.

7. We make you smell better. During your hygiene visit we eliminate many of the germs that live under your gum tissue and cause bad breath.

6. We save you money. By utilizing the latest dental technology (digital x-rays, mouth
cameras, and magnification glasses) we can help with early detection of tooth and gum
problems and save you the cost of gum surgery, root canals, and implants.

5. We clean in places you cannot. We clean under the gum line and between teeth where
most of the germs hide and cause dental disease. 40% of the bacteria in your mouth lives in
between your teeth.

4. We prevent pain. We identify tooth decay that can lead to nerve involvement and pain,
root canal, and tooth loss.

3. We save your teeth. Most tooth loss is from periodontal/gum disease. At each visit we
evaluate the health of your gums and bone with our periodontal screening. Periodontal
disease, like high blood pressure, is symptomless until it is in advanced stages.

2. We protect your loved ones. Studies have proven that the bacteria that cause dental
disease can be transmitted from person to person. Think about that the next time you kiss
someone!

1. We prolong life. Researchers have linked the inflammation and infection found in the
mouth to heart attacks, strokes, and Alzheimer’s. By reducing infection in your mouth we can
greatly improve your overall health!

```html
<!DOCTYPE html>
<html lang="en">
<head>
<meta charset="utf-8">
<title>It's Your Life – Top Ten Reasons</title>
<link rel="stylesheet" href="https://fonts.googleapis.com/css2?family=Montserrat:wght@400;600;700;800&family=Open+Sans:wght@400;600&family=Playfair+Display:wght@900&display=swap">
<style>
  :root {
    --navy: #1d2a5e;
    --navy-deep: #17224f;
    --sky: #4f9fd8;
    --sky-light: #7bbbe6;
    --ink: #1d2a5e;
    --paper: #ffffff;
    --band: #e9f2fa;
    --rule: #1d2a5e;
  }
  * { margin: 0; padding: 0; box-sizing: border-box; }
  html, body { width: 900px; height: 1200px; overflow: hidden; background: var(--paper); }
  .poster { position: relative; width: 900px; height: 1200px; background: var(--paper); font-family: "Open Sans", sans-serif; }

  .kicker { position: absolute; top: 14px; left: 0; width: 100%; text-align: center; font-family: "Montserrat", sans-serif; font-weight: 800; font-size: 34px; letter-spacing: 1px; color: var(--ink); }
  .title { position: absolute; top: 52px; left: 0; width: 100%; text-align: center; font-family: "Playfair Display", serif; font-weight: 900; font-size: 96px; line-height: 1; color: var(--ink); }
  .title-rule { position: absolute; top: 158px; left: 250px; width: 400px; height: 4px; background: var(--rule); border-radius: 2px; }

  .subhead { position: absolute; top: 176px; left: 0; width: 100%; text-align: center; font-family: "Montserrat", sans-serif; }
  .subhead .lead { font-weight: 600; font-size: 26px; color: var(--sky); letter-spacing: 0.5px; }
  .subhead .strong { display: inline-block; margin-top: 4px; font-weight: 800; font-size: 36px; color: var(--ink); position: relative; }
  .subhead .strong::before, .subhead .strong::after { content: ""; position: absolute; top: 50%; width: 70px; height: 3px; background: var(--rule); }
  .subhead .strong::before { right: calc(100% + 16px); }
  .subhead .strong::after { left: calc(100% + 16px); }

  .reasons { position: absolute; top: 262px; left: 66px; width: 768px; display: grid; grid-template-columns: repeat(3, 248px); grid-auto-rows: 262px; gap: 12px 12px; }
  .reason { position: relative; padding: 16px 16px; color: #fff; overflow: hidden; }
  .reason.navy { background: var(--navy); }
  .reason.sky { background: var(--sky); }
  .reason .num { font-family: "Montserrat", sans-serif; font-weight: 800; font-size: 44px; line-height: 1; }
  .reason .head { margin-top: 6px; font-family: "Montserrat", sans-serif; font-weight: 700; font-size: 14px; line-height: 1.2; text-transform: uppercase; }
  .reason .body { margin-top: 8px; width: 158px; font-size: 11px; line-height: 1.38; }
  .reason .icon { position: absolute; right: 14px; bottom: 22px; width: 56px; height: 64px; border-radius: 10px; background: rgba(255,255,255,0.22); }

  .top-reason { position: absolute; top: 1084px; left: 66px; width: 768px; height: 92px; background: var(--band); display: flex; align-items: center; padding: 0 20px; gap: 18px; }
  .top-reason .icon { width: 52px; height: 60px; border-radius: 10px; background: var(--sky-light); flex: none; }
  .top-reason .num { font-family: "Montserrat", sans-serif; font-weight: 800; font-size: 46px; color: var(--ink); line-height: 1; flex: none; }
  .top-reason .head { font-family: "Montserrat", sans-serif; font-weight: 800; font-size: 22px; color: var(--ink); flex: none; }
  .top-reason .body { font-size: 11.5px; line-height: 1.38; color: var(--ink); }
</style>
</head>
<body>
<div class="poster">
  <div class="kicker">IT’S NOT JUST A CLEANING.</div>
  <h1 class="title">It’s your life</h1>
  <div class="title-rule"></div>

  <div class="subhead">
    <div class="lead">TOP TEN REASONS WHY THIS IS</div>
    <div class="strong">MORE THAN ‘JUST A CLEANING’</div>
  </div>

  <div class="reasons">
    <div class="reason navy">
      <div class="num">10</div>
      <div class="head">We make you look better.</div>
      <p class="body">Healthy teeth and gums are more attractive. Recent studies show that the smile is the first thing people notice and that people with better looking teeth are more confident and successful.</p>
      <div class="icon" role="img" aria-label="Icon of a sparkling tooth"></div>
    </div>
    <div class="reason sky">
      <div class="num">9</div>
      <div class="head">We can relieve your headaches.</div>
      <p class="body">During your hygiene visit we evaluate for serious bite issues, many of which lead to muscle soreness, headaches, and migraines.</p>
      <div class="icon" role="img" aria-label="Icon of a dental chair"></div>
    </div>
    <div class="reason navy">
      <div class="num">8</div>
      <div class="head">We check for oral cancer.</div>
      <p class="body">Oral cancer kills 1 person per hour 24 hours a day. The death rate for oral cancer is higher than cancers we routinely hear about such as cervical, thyroid and skin cancer.</p>
      <div class="icon" role="img" aria-label="Icon of a dental mirror and probe"></div>
    </div>
    <div class="reason navy">
      <div class="num">7</div>
      <div class="head">We make you smell better.</div>
      <p class="body">During your hygiene visit we eliminate many of the germs that live under your gum tissue and cause bad breath.</p>
      <div class="icon" role="img" aria-label="Icon of fresh breath"></div>
    </div>
    <div class="reason sky">
      <div class="num">6</div>
      <div class="head">We save you money.</div>
      <p class="body">By utilizing the latest dental technology (digital x-rays, mouth cameras, and magnification glasses) we can help with early detection of tooth and gum problems and save you the cost of gum surgery, root canals, and implants.</p>
      <div class="icon" role="img" aria-label="Icon of savings"></div>
    </div>
    <div class="reason navy">
      <div class="num">5</div>
      <div class="head">We clean in places you cannot.</div>
      <p class="body">We clean under the gum line and between teeth where most of the germs hide and cause dental disease. 40% of the bacteria in your mouth lives in between your teeth.</p>
      <div class="icon" role="img" aria-label="Icon of dental cleaning tools"></div>
    </div>
    <div class="reason sky">
      <div class="num">4</div>
      <div class="head">We prevent pain.</div>
      <p class="body">We identify tooth decay that can lead to nerve involvement and pain, root canal, and tooth loss.</p>
      <div class="icon" role="img" aria-label="Icon of a tooth"></div>
    </div>
    <div class="reason navy">
      <div class="num">3</div>
      <div class="head">We save your teeth.</div>
      <p class="body">Most tooth loss is from periodontal gum disease. At each visit we evaluate the health of your gums and bone with our periodontal screening. Periodontal disease, like high blood pressure, is symptomless until it is in advanced stages.</p>
      <div class="icon" role="img" aria-label="Icon of a first aid kit"></div>
    </div>
    <div class="reason sky">
      <div class="num">2</div>
      <div class="head">We protect your loved ones.</div>
      <p class="body">Studies have proven that the bacteria that cause dental disease can be transmitted from person to person. Think about that the next time you kiss someone!</p>
      <div class="icon" role="img" aria-label="Icon of a family"></div>
    </div>
  </div>

  <div class="top-reason">
    <div class="icon" role="img" aria-label="Icon of a heartbeat"></div>
    <div class="num">1</div>
    <div class="head">WE PROLONG LIFE.</div>
    <p class="body">Researchers have linked the inflammation and infection found in the mouth to heart attacks, strokes, and Alzheimer’s. By reducing infection in your mouth we can greatly improve your overall health!</p>
  </div>
</div>
</body>
</html>
```